EB-5 Regional Center needs a Web design

Tallowmere Funding Partners is an expanding EB-r regional center. We have been successful in sponsoring multiple projects of third-party developers and placing EB-5, B-1, and Private Investments into multiple projects.

We are now partnering directly with project developers in the energy and healthcare to raise foreign capital for projects in those industries. The foreign capital is used as project equity and our collective balance sheets are used to guarantee debt to complete the funding of the projects.

We need a web site where we can post our company credentials, the bios of each partner, a document page for each of our projects where we can post specific project related documents which foreign investors can read, and we will need a section where foreign investors can fill out investor forms confirming that they are qualified investors and leaving their contact so that our agents and executives can make contact.

The final design should reflect the exceptional experience of the partners and our financial strength and stability.

We do have a logo we would want to use on the web design.

Target Market(s)

EB-5 Investors, B-1 Investors, Private Equity and other investors seeking quality investment in job creating US projects.

Coding

Number of Pages Required

5+ page

Font styles to use
Sans Serif

Requirements
Must have
• Pages to display company info, partner bios, projects completed, and a projects in-process page where we can post documents and info on projects for which we are seeking foreign investment. We also need a section where investors can enter their qualifying personal information and leave contact information for us.

```html
<!DOCTYPE html>
<html lang="en">
<head>
<meta charset="utf-8">
<title>Tallowmere Funding Partners</title>
<link href="https://fonts.googleapis.com/css2?family=Poppins:wght@300;400;500;600;700&display=swap" rel="stylesheet">
<style>
:root{
  --ink:#000;
  --text:#222;
  --muted:#777;
  --page:#f5f5f5;
  --white:#fff;
  --btn:#7b7b7b;
  --footer-grey:#7a7a7a;
  --line:#dcdcdc;
  --sky:#8fa3b3;
  --sky-dark:#3e5466;
}
*{box-sizing:border-box;margin:0;padding:0}
html,body{width:1200px;height:3698px;overflow:hidden}
body{position:relative;background:var(--page);font-family:'Poppins',sans-serif;color:var(--text)}
.abs{position:absolute}
.btn{position:absolute;background:var(--btn);color:#fff;border-radius:30px;display:flex;align-items:center;justify-content:center;font-weight:500;font-size:20px;text-transform:uppercase}
.photo{position:absolute}
/* header */
.hero-art{position:absolute;left:0;top:0}
.brand{position:absolute;display:flex;align-items:center;gap:12px}
.brand-dot{width:40px;height:40px;border-radius:50%;background:var(--muted)}
.brand-name{font-weight:500;color:var(--muted);font-size:22px;line-height:1.05;text-transform:uppercase;letter-spacing:.5px}
.nav{position:absolute;display:flex;gap:26px;font-size:14px;color:#333}
.hero-title{left:77px;top:212px;font-size:52px;font-weight:700;line-height:1.06;color:var(--ink)}
.hero-copy{left:77px;top:326px;width:370px;font-size:15px;line-height:27px;color:#555}
/* welcome */
.center{left:0;width:1200px;text-align:center}
.eyebrow{font-size:17px;color:var(--muted)}
.section-title{font-size:40px;font-weight:600;color:var(--ink);line-height:1.15;text-transform:uppercase}
.welcome-copy{left:639px;top:940px;width:400px;font-size:15px;line-height:27px;color:var(--muted)}
.welcome-copy p+p{margin-top:16px}
/* partners */
.partner-card{position:absolute;top:1507px;width:263px;height:376px;background:#fff;border-radius:6px;overflow:hidden;text-align:center}
.partner-photo{height:234px}
.partner-name{margin-top:32px;font-size:19px;font-weight:500;color:var(--ink)}
.partner-bio{margin-top:10px;font-size:15px;line-height:25px;color:var(--muted)}
/* projects */
.project-feature{left:158px;top:2144px;width:483px;height:492px;background:#000;border-radius:8px}
.project-caption{left:185px;top:2552px;color:#fff}
/* contact */
.field{position:absolute;height:56px;border:1px solid var(--line);background:#fff;border-radius:4px;font-size:15px;color:#999;padding:0 17px;display:flex;align-items:center}
.field.active{border:2px solid #222;color:#111}
/* footer */
.footer-band{left:0;top:3375px;width:1200px;height:152px;background:var(--footer-grey)}
.footer-tab{left:443px;top:3329px;width:313px;height:86px;background:#fff;border-radius:0 0 50px 50px;display:flex;align-items:center;justify-content:center}
.footer-nav{left:86px;top:3462px;display:flex;gap:26px;font-size:14px;color:#fff}
.social{position:absolute;width:46px;height:46px;border-radius:50%}
.contact-band{left:0;top:3527px;width:1200px;height:108px;background:#000;color:#fff}
.contact-item{position:absolute;display:flex;align-items:center;gap:12px;font-size:15px;line-height:27px}
</style>
</head>
<body>

<!-- HERO -->
<svg class="hero-art" width="1200" height="746" viewBox="0 0 836 520">
  <path d="M0,0 H836 V430 C700,475 520,485 400,475 C230,462 80,380 0,285 Z" fill="#fff"/>
  <path d="M285,0 C290,140 370,250 480,320 C580,390 650,460 836,405 L836,0 Z" fill="url(#sky)" stroke="#000" stroke-width="5" role="img" aria-label="Businessman looking over a city skyline through tall windows"/>
  <defs>
    <linearGradient id="sky" x1="0" y1="0" x2="0" y2="1">
      <stop offset="0" stop-color="#c9d2da"/>
      <stop offset=".55" stop-color="#7f93a4"/>
      <stop offset="1" stop-color="#2f4456"/>
    </linearGradient>
  </defs>
  <circle cx="210" cy="445" r="16" fill="#000"/>
  <path d="M213,438 L206,445 L213,452" fill="none" stroke="#fff" stroke-width="1.5"/>
  <circle cx="258" cy="459" r="23" fill="#7b7b7b"/>
  <path d="M255,450 L264,459 L255,468" fill="none" stroke="#fff" stroke-width="1.5"/>
</svg>

<div class="brand" style="left:77px;top:18px">
  <div class="brand-dot"></div>
  <div class="brand-name">Tallowmere<br>Funding Partners</div>
</div>
<nav class="nav" style="left:685px;top:37px">
  <span>HOME</span><span>ABOUT US</span><span>PARTNERS</span><span>PROJECTS</span><span>CONTACT</span>
</nav>

<h1 class="abs hero-title">FOREIGN<br>INVESTMENT</h1>
<p class="abs hero-copy">Lorem Ipsum is simply dummy text of the print and typesetting industry has been.</p>
<div class="btn" style="left:77px;top:395px;width:188px;height:57px">Contact Us</div>

<!-- WELCOME -->
<p class="abs center eyebrow" style="top:766px">Welcome To</p>
<h2 class="abs center section-title" style="top:801px">Tallowmere Funding<br>Partners</h2>
<div class="photo" role="img" aria-label="Hand placing a coin into a glass jar beside stacks of coins" style="left:175px;top:936px;width:406px;height:291px;border-radius:8px;background:linear-gradient(120deg,#e9e4d8,#c9b98f 55%,#8e9a8c)"></div>
<div class="abs welcome-copy">
  <p>Lorem Ipsum is simply dummy text of the printing and typesetting industry &nbsp;Lorem Ipsum.</p>
  <p>Lorem Ipsum is simply dummy text of the printing and typesetting industry. Lorem Ipsum has been the industry standard dummy text ever since the 1500s when an unknown printer took a galley Lorem Ipsum is simply dummy text of the printing.</p>
</div>
<div class="btn" style="left:637px;top:1170px;width:188px;height:57px">Learn More</div>

<!-- PARTNERS -->
<svg class="abs" style="left:0;top:1322px" width="1200" height="634">
  <polygon points="0,0 1043,0 933,634 0,634" fill="#000"/>
  <circle cx="1015" cy="119" r="34" fill="#7b7b7b"/>
  <path d="M1020,106 L1007,119 L1020,132" fill="none" stroke="#fff" stroke-width="2"/>
  <circle cx="1076" cy="146" r="23" fill="#000"/>
  <path d="M1073,137 L1082,146 L1073,155" fill="none" stroke="#fff" stroke-width="1.8"/>
</svg>
<h2 class="abs section-title" style="left:77px;top:1390px;color:#fff">Our Partner</h2>
<p class="abs" style="left:81px;top:1442px;font-size:15px;color:#fff">Lorem Ipsum is simply dummy text of the printing &amp; type</p>

<div class="partner-card" style="left:77px">
  <div class="partner-photo" role="img" aria-label="Portrait of a partner in a dark suit" style="background:linear-gradient(180deg,#d8dde0,#5a6068)"></div>
  <div class="partner-name">PARTNER NAME</div>
  <div class="partner-bio">Lorem Ipsum is simply the<br>dummy text of the.</div>
</div>
<div class="partner-card" style="left:373px">
  <div class="partner-photo" role="img" aria-label="Portrait of a partner in a navy blazer" style="background:linear-gradient(180deg,#cfe0e2,#3c4658)"></div>
  <div class="partner-name">PARTNER NAME</div>
  <div class="partner-bio">Lorem Ipsum is simply the<br>dummy text of the.</div>
</div>
<div class="partner-card" style="left:669px">
  <div class="partner-photo" role="img" aria-label="Portrait of a partner in a suit and white shirt" style="background:linear-gradient(180deg,#a9794f,#2e3a55)"></div>
  <div class="partner-name">PARTNER NAME</div>
  <div class="partner-bio">Lorem Ipsum is simply the<br>dummy text of the.</div>
</div>

<!-- PROJECTS -->
<svg class="abs" style="left:0;top:2636px" width="1200" height="180">
  <polygon points="0,0 1200,0 1200,30 600,178 0,30" fill="var(--page)"/>
  <polygon points="0,30 600,178 1200,30 1200,180 0,180" fill="#fff"/>
</svg>
<h2 class="abs center section-title" style="top:2026px">Our Projects</h2>
<p class="abs center" style="top:2080px;font-size:15px;color:#222">Lorem Ipsum is simply dummy text of the printing &amp; type</p>

<div class="abs project-feature"></div>
<div class="photo" role="img" aria-label="Businessman signing papers beside a small house model" style="left:166px;top:2150px;width:468px;height:376px;background:linear-gradient(160deg,#4a4c52,#b8c4c6 60%,#e6eaea)"></div>
<div class="abs project-caption">
  <div style="font-size:20px;font-weight:500">TALLOWMERE FUNDING PARTNERS</div>
  <div style="font-size:15px;margin-top:6px">Lorem Ipsum is simply dummy text of the printing &amp; type</div>
</div>
<div class="photo" role="img" aria-label="Solar panels in a green mountain valley" style="left:669px;top:2144px;width:371px;height:234px;border-radius:6px;background:linear-gradient(180deg,#c9d6de,#7a8f5a 50%,#2f56a6)"></div>
<div class="photo" role="img" aria-label="Stethoscope resting on a laptop keyboard" style="left:669px;top:2401px;width:373px;height:235px;border-radius:6px;background:linear-gradient(135deg,#e4e7ea,#9aa8b8 60%,#2a3548)"></div>
<div class="btn" style="left:488px;top:2661px;width:224px;height:57px">Explore More</div>

<!-- CONTACT -->
<div class="abs" style="left:0;top:2816px;width:1200px;height:513px;background:#fff"></div>
<h2 class="abs center section-title" style="top:2882px">Contact Us</h2>
<p class="abs center" style="top:2937px;font-size:15px;color:#666">If you have an any Question for Contact Us Today !</p>
<div class="field active" style="left:301px;top:2992px;width:292px">Name *</div>
<div class="field" style="left:603px;top:2992px;width:292px">Projects*</div>
<div class="field" style="left:301px;top:3070px;width:292px">Phone &nbsp;*</div>
<div class="field" style="left:603px;top:3070px;width:292px">Email *</div>
<div class="field" style="left:301px;top:3147px;width:594px">Message*</div>
<div class="btn" style="left:507px;top:3227px;width:188px;height:57px">Contact Us</div>

<!-- FOOTER -->
<div class="abs footer-band"></div>
<div class="abs footer-tab">
  <div class="brand" style="position:static">
    <div class="brand-dot"></div>
    <div class="brand-name">Tallowmere<br>Funding Partners</div>
  </div>
</div>
<nav class="abs footer-nav">
  <span>HOME</span><span>ABOUT US</span><span>PARTNERS</span><span>PROJECTS</span><span>CONTACT</span>
</nav>
<span class="abs" style="left:907px;top:3462px;font-size:14px;color:#fff">Follow Us On :</span>
<div class="social" style="left:1022px;top:3450px;background:#9a9a9a"></div>
<div class="social" style="left:1076px;top:3450px;border:2px solid #fff"></div>

<div class="abs contact-band">
  <div class="abs" style="left:77px;top:40px;font-size:30px;font-weight:600">STAY IN TOUCH</div>
  <div class="abs" style="left:77px;top:102px;width:244px;height:6px;background:#8a8a8a"></div>
  <div class="contact-item" style="left:418px;top:30px">
    <svg width="24" height="30" viewBox="0 0 24 30"><path d="M12,2 C6,2 2,6.5 2,12 C2,19 12,28 12,28 C12,28 22,19 22,12 C22,6.5 18,2 12,2 Z" fill="none" stroke="#fff" stroke-width="1.8"/><circle cx="12" cy="12" r="3.5" fill="none" stroke="#fff" stroke-width="1.8"/></svg>
    <span>Lorem ipsum simple<br>text print text.</span>
  </div>
  <div class="contact-item" style="left:680px;top:40px">
    <svg width="26" height="26" viewBox="0 0 24 24"><path d="M6.6,10.8 C8,13.6 10.4,16 13.2,17.4 L15.4,15.2 C15.7,14.9 16.1,14.8 16.4,15 C17.5,15.4 18.8,15.6 20,15.6 C20.6,15.6 21,16 21,16.6 V20 C21,20.6 20.6,21 20,21 C10.6,21 3,13.4 3,4 C3,3.4 3.4,3 4,3 H7.5 C8.1,3 8.5,3.4 8.5,4 C8.5,5.3 8.7,6.5 9.1,7.6 C9.2,7.9 9.1,8.3 8.9,8.6 Z" fill="#fff"/></svg>
    <span>555 014 2290</span>
  </div>
  <div class="contact-item" style="left:878px;top:40px">
    <svg width="24" height="20" viewBox="0 0 24 20"><rect x="1" y="2" width="22" height="16" rx="2" fill="#fff"/><path d="M2,4 L12,11 L22,4" fill="none" stroke="#000" stroke-width="1.8"/></svg>
    <span>info@tallowmere-example.com</span>
  </div>
</div>
<p class="abs center" style="top:3656px;font-size:14px;color:#555">©TALLOWMERE FUNDING PARTNERS - 2020 All rights reserved.</p>

</body>
</html>
```